Pagebook Ads for HOA Law Firm

We need to create certain ads for a Pagebook ads campaign. We are a law firm in Florida that represents homeowners against HOAs. We need to create the following ads:

1. Image Ads Specifications:

File Type: JPG or PNG
Ratio: 1.91:1 to 4:5
Resolution:
a) 1:1 ratio: 1080 x 1080 pixels
b) 4:5 ratio: 1080 x 1350 pixels
Maximum File Size: 30MB
Minimum Width: 600 pixels
Minimum Height:
a) 1:1 ratio: 600 pixels
b) 4:5 ratio: 750 pixels
Key Elements to Include in the Ads:

1) Headline: "HOA Violating Your Rights?"
2) Main Message: "We sue HOAs for Homeowners."
3) Firm Name: Lindqvist Harrow, P.A.
4) Website: www.covenantshieldcounsel.example
5) Phone Number: 1-800-555-0148
6) Florida Bar Compliance Statement: "Serving Homeowners in Florida with our main office in Miami-Dade."
7) Call-to-Action (CTA): Include a strong CTA such as “Contact us today for a consultation!”
8) Tone and Style: Professional yet approachable. The ad should emphasize trust, expertise, and our dedication to homeowners' rights.
9) Branding: Please use our firm's brand colors and fonts. Ensure that our logo is prominently placed within the ad.
10) Image Suggestions: Consider using images of Florida homes, frustrated homeowners, or visuals that evoke trust, protection, and legal authority.

```html
<!DOCTYPE html>
<html lang="en">
<head>
<meta charset="utf-8">
<title>HOA Homeowner Ads – Lindqvist Harrow, P.A.</title>
<link rel="stylesheet" href="https://fonts.googleapis.com/css2?family=Montserrat:wght@700;800&family=Roboto:wght@400;700&display=swap">
<style>
  :root {
    --navy: #121a8c;
    --navy-deep: #0d1470;
    --white: #ffffff;
    --ink: #2b2b2b;
    --stage: #ebeceb;
    --scene-a: #6065b8;
    --scene-b: #3c4299;
    --scene-c: #2f4a4a;
    --suit-a: #e4e6ec;
    --suit-b: #3a4872;
    --quote: #3c46c8;
  }
  * { box-sizing: border-box; margin: 0; padding: 0; }
  html, body { width: 1200px; height: 1200px; overflow: hidden; }
  body { background: var(--stage); position: relative; font-family: "Roboto", Arial, sans-serif; color: var(--ink); }

  .ad { position: absolute; background: var(--white); overflow: hidden; outline: 1px solid #555; }
  .ad--square { left: 60px; top: 276px; width: 518px; height: 648px; }
  .ad--wide { left: 622px; top: 160px; width: 518px; height: 519px; }
  .ad--banner { left: 622px; top: 747px; width: 518px; height: 292px; }

  .scene { position: absolute; left: 0; top: 0;
    background: linear-gradient(165deg, var(--scene-a) 0%, var(--scene-b) 50%, var(--scene-c) 100%); }
  .team { position: absolute; background: linear-gradient(180deg, var(--suit-a) 0%, #9aa3bd 45%, var(--suit-b) 100%); }

  .headline { position: absolute; font-family: "Montserrat", Arial, sans-serif; font-weight: 800;
    color: var(--white); text-transform: uppercase; letter-spacing: 0.5px; }
  .tagline { position: absolute; font-family: "Montserrat", Arial, sans-serif; font-weight: 800; color: var(--white); }

  .band { position: absolute; left: 0; background: var(--navy); color: var(--white); }
  .site { position: absolute; color: var(--white); white-space: nowrap; }
  .phone { position: absolute; color: var(--white); font-weight: 700; white-space: nowrap; }

  .brand { position: absolute; display: flex; align-items: center; gap: 8px;
    font-family: "Montserrat", Arial, sans-serif; font-weight: 700; color: var(--navy); text-transform: uppercase; white-space: nowrap; }
  .brand__mark { background: var(--navy); flex: none; }

  .compliance { position: absolute; text-align: center; color: var(--ink); }
  .compliance b { font-weight: 700; }

  /* square ad */
  .ad--square .scene { width: 518px; height: 348px; }
  .ad--square .scene-rule { position: absolute; left: 0; top: 348px; width: 518px; height: 5px; background: var(--navy); }
  .ad--square .headline { left: 24px; top: 30px; font-size: 40px; line-height: 45px; }
  .ad--square .tagline { left: 24px; top: 222px; font-size: 21px; line-height: 31px; }
  .ad--square .cta { position: absolute; left: 138px; top: 325px; width: 242px; height: 52px; background: var(--navy);
    clip-path: polygon(10% 0, 90% 0, 100% 50%, 90% 100%, 10% 100%, 0 50%);
    color: var(--white); font-size: 17px; line-height: 20px; text-align: center; padding-top: 6px; }
  .ad--square .compliance { left: 0; width: 518px; top: 385px; font-size: 17px; line-height: 21px; }
  .ad--square .brand { left: 28px; top: 498px; font-size: 15px; }
  .ad--square .brand__mark { width: 14px; height: 14px; }
  .ad--square .band { top: 568px; width: 518px; height: 80px; }
  .ad--square .site { left: 19px; top: 583px; font-size: 14px; }
  .ad--square .phone { left: 19px; top: 606px; font-size: 27px; }
  .ad--square .team { left: 302px; top: 438px; width: 216px; height: 210px; }

  /* wide ad */
  .ad--wide .scene { width: 518px; height: 248px; }
  .ad--wide .headline { left: 19px; top: 12px; font-size: 35px; line-height: 40px; }
  .ad--wide .tagline { left: 19px; top: 186px; font-size: 19px; line-height: 27px; }
  .ad--wide .cta { position: absolute; left: 0; top: 255px; width: 241px; height: 52px; background: var(--navy);
    clip-path: polygon(0 0, 88% 0, 100% 50%, 88% 100%, 0 100%);
    color: var(--white); font-size: 17px; line-height: 20px; padding: 6px 0 0 8px; }
  .ad--wide .serve-frame { position: absolute; left: 212px; top: 248px; }
  .ad--wide .compliance { left: 250px; width: 268px; top: 250px; font-size: 16px; line-height: 20px; }
  .ad--wide .brand { left: 36px; top: 388px; font-size: 14px; }
  .ad--wide .brand__mark { width: 13px; height: 13px; }
  .ad--wide .band { top: 440px; width: 518px; height: 79px; }
  .ad--wide .site { left: 19px; top: 457px; font-size: 14px; }
  .ad--wide .phone { left: 19px; top: 480px; font-size: 28px; }
  .ad--wide .team { left: 300px; top: 320px; width: 218px; height: 199px; }

  /* banner ad */
  .ad--banner .scene { width: 316px; height: 149px; }
  .ad--banner .headline { left: 24px; top: 10px; font-size: 20px; line-height: 19px; }
  .ad--banner .tagline { left: 24px; top: 114px; font-size: 11px; line-height: 16px; }
  .ad--banner .quote-panel { position: absolute; left: 316px; top: 0; width: 202px; height: 149px; background: var(--navy); }
  .ad--banner .quote { position: absolute; font-family: Georgia, serif; font-weight: 700; font-size: 44px; line-height: 1; color: var(--quote); }
  .ad--banner .quote--open { left: 330px; top: 6px; }
  .ad--banner .quote--close { right: 8px; top: 106px; }
  .ad--banner .compliance { left: 316px; width: 195px; top: 26px; font-size: 16px; line-height: 19px; color: var(--white); }
  .ad--banner .brand { left: 24px; top: 213px; font-size: 12px; gap: 6px; }
  .ad--banner .brand__mark { width: 11px; height: 11px; }
  .ad--banner .cta-hex { position: absolute; left: 222px; top: 164px; width: 82px; height: 91px; }
  .ad--banner .cta-hex__text { position: absolute; left: 222px; top: 193px; width: 82px; text-align: center;
    color: var(--white); font-size: 10px; line-height: 12px; }
  .ad--banner .band { top: 264px; width: 322px; height: 28px; }
  .ad--banner .contact-line { position: absolute; left: 12px; top: 271px; color: var(--white); font-size: 11px; white-space: nowrap; }
  .ad--banner .contact-line b { margin-left: 3px; }
  .ad--banner .team { left: 322px; top: 149px; width: 196px; height: 143px; }
</style>
</head>
<body>

  <section class="ad ad--square">
    <div class="scene" role="img" aria-label="Florida house with a stressed homeowner at a desk, under a blue tint"></div>
    <div class="scene-rule"></div>
    <h1 class="headline">HOA<br>Violating<br>Your<br>Rights?</h1>
    <p class="tagline">We sue HOAs<br>for Homeowners.</p>
    <div class="cta">Contact us <b>today</b> for<br>a consultation!</div>
    <p class="compliance"><b>Serving Homeowners</b> in Florida<br>with our main office in <b>Miami-Dade.</b></p>
    <div class="brand"><span class="brand__mark"></span>Lindqvist Harrow, P.A.</div>
    <div class="band"></div>
    <p class="site">www.covenantshieldcounsel.example</p>
    <p class="phone">1-800-555-0148</p>
    <div class="team" role="img" aria-label="Portrait of the firm's two attorneys in suits"></div>
  </section>

  <section class="ad ad--wide">
    <div class="scene" role="img" aria-label="Florida house with a stressed homeowner, under a blue tint"></div>
    <h2 class="headline">HOA<br>Violating<br>Your<br>Rights?</h2>
    <p class="tagline">We sue HOAs<br>for Homeowners.</p>
    <div class="cta">Contact us <b>today</b> for<br>a consultation!</div>
    <svg class="serve-frame" width="306" height="66" viewBox="0 0 306 66">
      <polygon points="29,1 305,1 305,65 29,65 1,33" fill="#ffffff" stroke="#121a8c" stroke-width="1.5"/>
    </svg>
    <p class="compliance"><b>Serving Homeowners</b><br>in Florida with our main office<br>in <b>Miami-Dade.</b></p>
    <div class="brand"><span class="brand__mark"></span>Lindqvist Harrow, P.A.</div>
    <div class="band"></div>
    <p class="site">www.covenantshieldcounsel.example</p>
    <p class="phone">1-800-555-0148</p>
    <div class="team" role="img" aria-label="Portrait of the firm's two attorneys in suits"></div>
  </section>

  <section class="ad ad--banner">
    <div class="scene" role="img" aria-label="Florida house with a stressed homeowner, under a blue tint"></div>
    <h2 class="headline">HOA<br>Violating<br>Your<br>Rights?</h2>
    <p class="tagline">We sue HOAs<br>for Homeowners.</p>
    <div class="quote-panel"></div>
    <span class="quote quote--open">&ldquo;</span>
    <p class="compliance"><b>Serving<br>Homeowners</b><br>in Florida with<br>our main office<br>in <b>Miami-Dade.</b></p>
    <span class="quote quote--close">&rdquo;</span>
    <div class="brand"><span class="brand__mark"></span>Lindqvist Harrow, P.A.</div>
    <svg class="cta-hex" viewBox="0 0 82 91">
      <polygon points="41,0 82,22.75 82,68.25 41,91 0,68.25 0,22.75" fill="#121a8c"/>
      <polygon points="41,6 77,26 77,65 41,85 5,65 5,26" fill="none" stroke="#ffffff" stroke-width="1"/>
    </svg>
    <p class="cta-hex__text">Contact us<br><b>today</b> for a<br>consultation!</p>
    <div class="band"></div>
    <p class="contact-line">www.covenantshieldcounsel.example &nbsp;|&nbsp;<b>1-800-555-0148</b></p>
    <div class="team" role="img" aria-label="Portrait of the firm's two attorneys in suits"></div>
  </section>

</body>
</html>
```